Letterhead & Email Signature Design

Kindly assist redesign this letterhead as well as the Email signature. I have uploaded the current designs that needs some new look

```html
<!DOCTYPE html>
<html lang="en">
<head>
<meta charset="utf-8">
<title>Ravelo Dune Inc. – Letterhead &amp; Email Signature</title>
<link rel="stylesheet" href="https://fonts.googleapis.com/css2?family=Arimo:wght@400&family=Poppins:wght@400;500;600&display=swap">
<style>
  :root{
    --backdrop:#d9dadc;
    --paper:#f0f0f1;
    --brand:#636465;
    --ink:#4a4a4b;
    --ink-soft:#5a5a5b;
    --rule:#8a8a8b;
    --icon-cut:#f0f0f1;
  }
  *{box-sizing:border-box;margin:0;padding:0}
  html,body{width:1200px;height:968px;overflow:hidden}
  body{background:var(--backdrop);position:relative;font-family:"Poppins",sans-serif;color:var(--ink)}
  .sheet{position:absolute;background:var(--paper);overflow:hidden}
  .corner-dot{position:absolute;border-radius:50%;background:var(--brand)}
  .brand{position:absolute;display:flex;align-items:center;justify-content:center;text-align:center}
  .brand-name{font-family:"Poppins",sans-serif;font-weight:500;color:var(--brand);line-height:1.15;white-space:nowrap}

  .contact-line{display:flex;align-items:center;gap:4px}
  .contact-line svg{width:7px;height:7px;fill:var(--ink-soft);flex:none}

  /* Letterhead */
  .letterhead{left:90px;top:74px;width:573px;height:804px}
  .letterhead .brand{left:0;right:0;top:78px;height:36px}
  .letterhead .brand-name{font-size:24px}
  .salutation{position:absolute;left:43px;top:201px;font-family:"Arimo",sans-serif;font-size:13.5px;color:var(--ink-soft)}
  .letter-body{position:absolute;left:43px;top:242px;width:488px;font-family:"Arimo",sans-serif;font-size:8px;line-height:12.2px;color:var(--ink-soft);text-align:justify}
  .letter-body p{margin-bottom:12.4px}
  .closing{position:absolute;left:42px;top:512px;font-family:"Arimo",sans-serif;font-size:8px;color:var(--ink-soft)}
  .signature{position:absolute;left:40px;top:540px;width:164px;height:46px;background:linear-gradient(90deg,#e4e4e5,#dcdcdd)}
  .letter-footer{position:absolute;left:43px;top:643px;font-size:8.2px;line-height:10.2px;color:var(--ink-soft)}
  .letter-footer strong{font-weight:600}
  .letter-footer .gap{height:10px}
  .letter-footer .gap-sm{height:4px}
  .legal{position:absolute;left:41px;top:747px;font-size:8.2px;line-height:14.5px;color:var(--ink-soft)}
  .legal strong{font-weight:600}

  /* Cards */
  .card-name{font-weight:500;color:var(--ink);letter-spacing:.2px}
  .card-role{color:var(--ink-soft)}
  .card-block{color:var(--ink-soft)}
  .card-block strong{font-weight:600}
  .divider{position:absolute;width:1px;background:var(--rule)}

  .card-portrait{left:694px;top:297px;width:176px;height:290px}
  .card-portrait .brand{left:0;right:0;top:44px;height:20px}
  .card-portrait .brand-name{font-size:14px}
  .card-portrait .info{position:absolute;left:22px;top:110px;font-size:8.4px;line-height:10.2px}
  .card-portrait .card-name{font-size:11.2px;line-height:13px}
  .card-portrait .card-block{margin-top:9px}
  .card-portrait .contacts{margin-top:9px}

  .card-landscape{left:694px;top:612px;width:404px;height:154px}
  .card-landscape .brand{left:10px;width:148px;top:68px;height:20px}
  .card-landscape .brand-name{font-size:14px}
  .card-landscape .divider{left:156px;top:22px;height:109px}
  .card-landscape .info{position:absolute;left:176px;top:18px;font-size:8.6px;line-height:10.2px}
  .card-landscape .card-name{font-size:12.4px;line-height:14px}
  .card-landscape .card-block{margin-top:6px}
  .card-landscape .contacts{margin-top:3px}

  .email-signature{left:694px;top:790px;width:404px;height:88px}
  .email-signature .brand{left:4px;width:80px;top:36px;height:14px}
  .email-signature .brand-name{font-size:9px}
  .email-signature .divider{height:48px;top:20px}
  .email-signature .divider.first{left:84px}
  .email-signature .divider.second{left:238px}
  .email-signature .person{position:absolute;left:98px;top:19px;font-size:7.4px;line-height:9px}
  .email-signature .card-name{font-size:8.6px;line-height:10px}
  .email-signature .contacts{margin-top:3px}
  .email-signature .office{position:absolute;left:247px;top:16px;font-size:7.2px;line-height:9px}
</style>
</head>
<body>

<!-- Letterhead -->
<section class="sheet letterhead">
  <div class="brand"><span class="brand-name">Ravelo Dune Inc.</span></div>

  <p class="salutation">Dear Mr. Carter,</p>

  <div class="letter-body">
    <p>Lorem ipsum dolor sit amet, consectetur adipiscing elit. Donec orci purus, luctus vitae dignissim eu, iaculis sed purus. Vivamus faucibus, ipsum nec aliquet viverra, leo mauris condimentum ligula, sit amet sagittis enim ligula quis arcu. Nam egestas tortor id nisi porttitor mattis. In tortor ante, ultricies in suscipit a, tempus non massa. Vivamus et auctor mi. Fusce vel massa nulla. Phasellus nec eros mauris, et scelerisque orci.</p>
    <p>Donec malesuada orci vitae nulla accumsan porta a id massa. Quisque accumsan iaculis magna sit amet fringilla. Maecenas consequat, magna eget tincidunt semper, odio nibh rutrum mi, id feugiat ante nisi eu risus. Vestibulum nunc orci, rhoncus a placerat in, ultricies in mi. Cras mattis varius eros, vel fringilla nisi suscipit eget. Quisque scelerisque sagittis nulla at porttitor.</p>
    <p>Sed id augue vitae urna euismod commodo aliquet a quam. Pellentesque arcu velit, cursus et malesuada ut, consequat et diam. Nullam erat sem, rhoncus id ullamcorper vitae, rhoncus et arcu. In ultricies ultricies nulla, ut rutrum nisi iaculis at. Donec eu magna a metus ornare faucibus. Fusce aliquet faucibus ultricies. Morbi semper, est id tincidunt gravida, sem arcu adipiscing lacus, ac bibendum nulla leo eu purus. Quisque nec diam sed risus consectetur a ccumsan quis quis nibh. Vestibulum id purus lorem.</p>
    <p>It is a long established fact that a reader will be distracted by the readable content of a page when looking at its layout. The point of using Lorem Ipsum is that it has a more-or-less normal distribution of letters, as opposed to using 'Content here, content here', making it look like readable English. Many desktop publishing packages</p>
    <p>ada ut, consequat et diam. Nullam erat sem, rhoncus id ullamcorper vitae, rhoncus et arcu. In ultricies ultricies nulla, ut rutrum nisi iaculis at. Donec eu magna a metus ornare faucibus. Fusce aliquet faucibus ultricies. Morbi semper,</p>
  </div>

  <p class="closing">Sincerely,</p>
  <div class="signature" role="img" aria-label="Handwritten signature of the sender"></div>

  <div class="letter-footer">
    <strong>RAVELO DUNE INC.</strong><br>
    The Linden Office Park, Ground Floor, Building A<br>
    412 Maple Road, Brookfield, 0094
    <div class="gap"></div>
    Postel Address<br>
    PO Box 48, Oakhill, 0172
    <div class="gap-sm"></div>
    <div class="contact-line"><svg viewBox="0 0 10 10"><path d="M2 0.5 L3.6 0.5 L4.3 2.8 L3.2 3.7 Q4.2 5.8 6.3 6.8 L7.2 5.7 L9.5 6.4 L9.5 8 Q9.5 9.5 8 9.5 Q1 9 0.5 2 Q0.5 0.5 2 0.5Z"/></svg>012 555 0148</div>
    <div class="contact-line"><svg viewBox="0 0 10 10"><rect x="2.5" y="0.5" width="5" height="3"/><rect x="0.5" y="3.5" width="9" height="4"/><rect x="2.5" y="6.5" width="5" height="3"/></svg>012 555 0163</div>
    <div class="contact-line"><svg viewBox="0 0 10 10"><path d="M0.5 2 L9.5 2 L9.5 8.5 L0.5 8.5Z M1 2.5 L5 5.6 L9 2.5" stroke="#f0f0f1" stroke-width="0.8"/></svg>info@ravelodune.co.za</div>
  </div>

  <div class="legal">
    <strong>ATTORNEYS | CONVEYANCERS | NOTARIES ,</strong> Reg. No: 2011/004318/21<br>
    <strong>DIRECTORS:</strong> T R Ruvolo B. PROC LLB (Hons) | L Dune (LLB)&nbsp; <strong>CONSULTANT:</strong> MP Dune
  </div>

  <span class="corner-dot" style="left:479px;top:731px;width:118px;height:118px"></span>
</section>

<!-- Business card, portrait -->
<section class="sheet card-portrait">
  <div class="brand"><span class="brand-name">Ravelo Dune Inc.</span></div>
  <div class="info">
    <div class="card-name">TENDAI RUVOLO</div>
    <div class="card-role">Director</div>
    <div class="card-block">
      <strong>RAVELO DUNE INC.</strong><br>
      The Linden Office Park<br>
      Ground Floor, Building A<br>
      412 Maple Road,<br>
      Brookfield, 0094<br>
      <strong>Postel Address</strong><br>
      PO Box 48, Oakhill, 0172
    </div>
    <div class="card-block contacts">
      <div class="contact-line"><svg viewBox="0 0 10 10"><path d="M2 0.5 L3.6 0.5 L4.3 2.8 L3.2 3.7 Q4.2 5.8 6.3 6.8 L7.2 5.7 L9.5 6.4 L9.5 8 Q9.5 9.5 8 9.5 Q1 9 0.5 2 Q0.5 0.5 2 0.5Z"/></svg>+27 12 555 0148</div>
      <div class="contact-line"><svg viewBox="0 0 10 10"><path d="M0.5 2 L9.5 2 L9.5 8.5 L0.5 8.5Z M1 2.5 L5 5.6 L9 2.5" stroke="#f0f0f1" stroke-width="0.8"/></svg>tendai@ravelodune.co.za</div>
      <div class="contact-line"><svg viewBox="0 0 10 10"><circle cx="5" cy="5" r="4.5"/><path d="M0.5 5 H9.5 M5 0.5 Q2 5 5 9.5 M5 0.5 Q8 5 5 9.5" stroke="#f0f0f1" stroke-width="0.7" fill="none"/></svg>www.ravelodune.co.za</div>
    </div>
  </div>
  <span class="corner-dot" style="left:137px;top:259px;width:76px;height:76px"></span>
</section>

<!-- Business card, landscape -->
<section class="sheet card-landscape">
  <div class="brand"><span class="brand-name">Ravelo Dune Inc.</span></div>
  <span class="divider"></span>
  <div class="info">
    <div class="card-name">TENDAI RUVOLO</div>
    <div class="card-role">Director</div>
    <div class="card-block">
      <strong>RAVELO DUNE INC.</strong><br>
      The Linden Office Park, Ground Floor, Building A<br>
      412 Maple Road, Brookfield, 0094<br>
      <strong>Postel Address</strong><br>
      PO Box 48, Oakhill, 0172
    </div>
    <div class="card-block contacts">
      <div class="contact-line"><svg viewBox="0 0 10 10"><path d="M2 0.5 L3.6 0.5 L4.3 2.8 L3.2 3.7 Q4.2 5.8 6.3 6.8 L7.2 5.7 L9.5 6.4 L9.5 8 Q9.5 9.5 8 9.5 Q1 9 0.5 2 Q0.5 0.5 2 0.5Z"/></svg>+27 12 555 0148</div>
      <div class="contact-line"><svg viewBox="0 0 10 10"><path d="M0.5 2 L9.5 2 L9.5 8.5 L0.5 8.5Z M1 2.5 L5 5.6 L9 2.5" stroke="#f0f0f1" stroke-width="0.8"/></svg>tendai@ravelodune.co.za</div>
      <div class="contact-line"><svg viewBox="0 0 10 10"><circle cx="5" cy="5" r="4.5"/><path d="M0.5 5 H9.5 M5 0.5 Q2 5 5 9.5 M5 0.5 Q8 5 5 9.5" stroke="#f0f0f1" stroke-width="0.7" fill="none"/></svg>www.ravelodune.co.za</div>
    </div>
  </div>
  <span class="corner-dot" style="left:365px;top:123px;width:80px;height:80px"></span>
</section>

<!-- Email signature -->
<section class="sheet email-signature">
  <div class="brand"><span class="brand-name">Ravelo Dune Inc.</span></div>
  <span class="divider first"></span>
  <div class="person">
    <div class="card-name">TENDAI RUVOLO</div>
    <div class="card-role">Director</div>
    <div class="card-block contacts">
      <div class="contact-line"><svg viewBox="0 0 10 10"><path d="M2 0.5 L3.6 0.5 L4.3 2.8 L3.2 3.7 Q4.2 5.8 6.3 6.8 L7.2 5.7 L9.5 6.4 L9.5 8 Q9.5 9.5 8 9.5 Q1 9 0.5 2 Q0.5 0.5 2 0.5Z"/></svg>+27 12 555 0148</div>
      <div class="contact-line"><svg viewBox="0 0 10 10"><path d="M0.5 2 L9.5 2 L9.5 8.5 L0.5 8.5Z M1 2.5 L5 5.6 L9 2.5" stroke="#f0f0f1" stroke-width="0.8"/></svg>tendai@ravelodune.co.za</div>
      <div class="contact-line"><svg viewBox="0 0 10 10"><circle cx="5" cy="5" r="4.5"/><path d="M0.5 5 H9.5 M5 0.5 Q2 5 5 9.5 M5 0.5 Q8 5 5 9.5" stroke="#f0f0f1" stroke-width="0.7" fill="none"/></svg>www.ravelodune.co.za</div>
    </div>
  </div>
  <span class="divider second"></span>
  <div class="office card-block">
    <strong>RAVELO DUNE INC.</strong><br>
    The Linden Office Park<br>
    Ground Floor, Building A<br>
    412 Maple Road,Brookfield, 0094<br>
    <strong>Postel Address</strong><br>
    PO Box 48, Oakhill, 0172
  </div>
  <span class="corner-dot" style="left:374px;top:65px;width:56px;height:56px"></span>
</section>

</body>
</html>
```